Computer company startup need wordpress template

I am looking for a new design that is fresh, bold and stands out from the crowd for an IT company called Torvane Computers. We specialise in consumer and small business IT.

It will have to be mobile friendly, viewable on all devices. I need a template that i can work with and that will give our site a professional look and feel but not look like every other site out there.

To see what text will be on final site, see www.torvanecomputers-demo.com.au, i will change wording, but it is pretty close to what it's meant to be.

I have supplied logo and the main colours on car, business cards etc is black, red (and shades thereof) and white.

I am visualiing some home page with "Welcome to Torvane Computers, how may we help you today?" then 4 cool looking buttons below which says:

1. Residential computer / network issues
2. Business computer / network issues
3. Home Networking
4. New home networking

These buttons will then take you to the correct page which i will flesh out from the template. All pages need have sections for my support links etc.

Website built from template will have 5-6 pages max.

If anyone need any additional direction, please send me a message and i will answer.

Target Market(s)

Consumer and small business (1-20 employees) customers

Industry/Entity Type

It Company

Requirements
Must have
• professional look and feel

```html
<!DOCTYPE html>
<html lang="en">
<head>
<meta charset="utf-8">
<title>Torvane Computers</title>
<link href="https://fonts.googleapis.com/css2?family=Bebas+Neue&family=Open+Sans:wght@300;400;600;700&display=swap" rel="stylesheet">
<style>
:root{
  --red:#e8232b;
  --red-dark:#b8141b;
  --ink:#333333;
  --muted:#6b6b6b;
  --light:#f2f2f2;
  --footer:#262626;
  --footer-bar:#1a1a1a;
  --white:#ffffff;
  --badge:#a9a9a9;
}
*{margin:0;padding:0;box-sizing:border-box}
html,body{width:723px;height:1200px;overflow:hidden}
body{font-family:"Open Sans",Arial,sans-serif;color:var(--ink);background:var(--white);position:relative}

.site-header{height:86px;display:flex;align-items:center;justify-content:space-between;padding:0 36px;border-top:4px solid var(--red)}
.brand{display:flex;align-items:center;gap:10px}
.brand-dot{width:14px;height:14px;border-radius:50%;background:var(--red)}
.brand-name{font-family:"Bebas Neue",Impact,sans-serif;font-size:34px;color:var(--red);letter-spacing:1px}
.main-nav{display:flex;gap:6px}
.main-nav a{font-size:13px;color:var(--ink);text-decoration:none;padding:8px 11px;text-transform:uppercase}
.main-nav a.active{color:var(--red);border:1px solid var(--red)}

.hero{position:relative;height:276px;background:linear-gradient(90deg,#f4f4f4 0%,#ececec 100%);overflow:hidden}
.hero-photo{position:absolute;right:0;top:0;width:400px;height:276px;background:linear-gradient(135deg,#f7f7f7 0%,#e3e3e3 45%,#c9c2bf 70%,#8a6a5e 100%)}
.hero-copy{position:absolute;left:44px;top:86px}
.hero-question{font-size:26px;font-weight:300;color:var(--ink)}
.hero-call{font-family:"Bebas Neue",Impact,sans-serif;font-size:52px;color:var(--red);line-height:1;margin-top:14px}
.hero-phone{display:flex;align-items:center;gap:10px;font-family:"Bebas Neue",Impact,sans-serif;font-size:52px;color:var(--red);line-height:1}

.welcome{height:240px;text-align:center;padding:28px 70px 0}
.welcome h1{font-size:30px;font-weight:300;color:var(--red);letter-spacing:1px;white-space:nowrap;line-height:1.3}
.welcome p{font-size:9.5px;line-height:1.6;color:var(--muted);margin-top:14px}
.welcome p + p{margin-top:10px}
.btn-more{display:inline-block;margin-top:14px;font-size:11px;font-weight:700;color:var(--red);border:1px solid var(--red);padding:6px 12px;text-transform:uppercase;line-height:1.3}

.services{height:190px;background:linear-gradient(90deg,var(--red-dark) 0%,var(--red) 50%,var(--red-dark) 100%);display:flex}
.service{flex:1;display:flex;flex-direction:column;align-items:center;justify-content:center;border-right:1px solid rgba(255,255,255,.18)}
.service:last-child{border-right:none}
.service-icon{width:66px;height:54px;border-radius:8px;background:linear-gradient(180deg,#ffffff 0%,#cfd8e0 100%)}
.service-label{margin-top:14px;font-size:13px;color:var(--white);text-align:center;line-height:1.3}

.partners{height:166px;padding:26px 46px 0;display:flex;flex-direction:column;gap:22px}
.partner-row{display:flex;justify-content:space-between;align-items:center}
.partner-row.short{justify-content:center;gap:56px}
.badge{height:36px;width:72px;border-radius:4px;background:var(--badge)}

.site-footer{position:absolute;left:0;top:958px;width:723px;height:214px;background:var(--footer);color:#cfcfcf;display:flex;padding:22px 30px 0;gap:26px}
.footer-col h3{font-size:17px;font-weight:400;color:var(--white);margin-bottom:14px}
.links{width:150px;flex:none}
.links li{list-style:none;font-size:10px;line-height:1.75}
.links li.active{color:var(--red)}
.news{width:200px;flex:none}
.news-item{margin-bottom:12px}
.news-date{font-size:8px;color:#9a9a9a}
.news-title{font-size:10px;color:var(--red);margin:1px 0}
.news-text{font-size:8.5px;line-height:1.5}
.contact{flex:1;min-width:0}
.contact li{list-style:none;display:flex;align-items:flex-start;gap:8px;font-size:9px;line-height:1.4;margin-bottom:7px;white-space:nowrap}
.contact svg{flex:none}
.social{display:flex;gap:12px;margin-top:8px}
.social span{width:24px;height:24px;border-radius:50%;border:1px solid #8a8a8a}

.footer-bar{position:absolute;left:0;bottom:0;width:723px;height:28px;background:var(--footer-bar);border-top:3px solid var(--red);text-align:center;font-size:9px;color:#bdbdbd;line-height:25px}
.footer-bar strong{color:var(--red);font-weight:600}
</style>
</head>
<body>

<header class="site-header">
  <div class="brand"><span class="brand-dot"></span><span class="brand-name">Torvane Computers</span></div>
  <nav class="main-nav">
    <a class="active">Home</a><a>About</a><a>Services</a><a>FAQ</a><a>Contact</a>
  </nav>
</header>

<section class="hero">
  <div class="hero-photo" role="img" aria-label="Photo of a smiling support consultant working at a laptop in a bright office"></div>
  <div class="hero-copy">
    <p class="hero-question">How may we help you today?</p>
    <p class="hero-call">Call us on</p>
    <p class="hero-phone">
      <svg width="40" height="40" viewBox="0 0 24 24" aria-hidden="true"><path fill="#e8232b" d="M6.6 10.8a15.1 15.1 0 0 0 6.6 6.6l2.2-2.2a1 1 0 0 1 1-.25 11.4 11.4 0 0 0 3.6.57 1 1 0 0 1 1 1V20a1 1 0 0 1-1 1A17 17 0 0 1 3 4a1 1 0 0 1 1-1h3.5a1 1 0 0 1 1 1c0 1.25.2 2.45.57 3.57a1 1 0 0 1-.25 1z"/></svg>
      0491 570 156
    </p>
  </div>
</section>

<section class="welcome">
  <h1>WELCOME TO TORVANE COMPUTERS</h1>
  <p>Torvane Computers deliver expert onsite computer services to small businesses and home owners in Southern Tasmania. We specialise in IT security, custom built computers and general computer repair.</p>
  <p>Our expert staff will also help you with training and pre-purchase advice to make sure your business or family has the right setup, and will also future proof you in the areas where your system will be relied on the most.</p>
  <span class="btn-more">Read more</span>
</section>

<section class="services">
  <div class="service"><div class="service-icon" role="img" aria-label="Illustration of a desktop computer"></div><p class="service-label">Residential computer<br>/ network issues</p></div>
  <div class="service"><div class="service-icon" role="img" aria-label="Illustration of business computers"></div><p class="service-label">Business computer /<br>network issues</p></div>
  <div class="service"><div class="service-icon" role="img" aria-label="Illustration of a house"></div><p class="service-label">Home<br>Networking</p></div>
  <div class="service"><div class="service-icon" role="img" aria-label="Illustration of a new home"></div><p class="service-label">New Home<br>networking</p></div>
</section>

<section class="partners" aria-label="Brands we support">
  <div class="partner-row">
    <span class="badge"></span><span class="badge"></span><span class="badge"></span><span class="badge"></span><span class="badge"></span><span class="badge"></span><span class="badge"></span>
  </div>
  <div class="partner-row short">
    <span class="badge" style="width:90px"></span><span class="badge" style="width:110px"></span><span class="badge"></span>
  </div>
</section>

<footer class="site-footer">
  <div class="footer-col links">
    <h3>Useful Links</h3>
    <ul><li class="active">Home</li><li>About</li><li>Services</li><li>Faq</li><li>News</li><li>Contact</li></ul>
  </div>
  <div class="footer-col news">
    <h3>Latest News</h3>
    <div class="news-item"><p class="news-date">10 Mar 2015</p><p class="news-title">News Title</p><p class="news-text">Lorem Ipsum is simply dummy text of the printing and typesetting industry.</p></div>
    <div class="news-item"><p class="news-date">10 Mar 2015</p><p class="news-title">News Title</p><p class="news-text">Lorem Ipsum is simply dummy text of the printing and typesetting industry.</p></div>
  </div>
  <div class="footer-col contact">
    <h3>Contact Info</h3>
    <ul>
      <li><svg width="12" height="12" viewBox="0 0 24 24"><path fill="#e8232b" d="M12 2a7 7 0 0 0-7 7c0 5 7 13 7 13s7-8 7-13a7 7 0 0 0-7-7zm0 9.5A2.5 2.5 0 1 1 12 6.5a2.5 2.5 0 0 1 0 5z"/></svg><span>24 Harrow Lane<br>Lindisfarne TAS 7018</span></li>
      <li><svg width="12" height="12" viewBox="0 0 24 24"><path fill="#e8232b" d="M6.6 10.8a15.1 15.1 0 0 0 6.6 6.6l2.2-2.2a1 1 0 0 1 1-.25 11.4 11.4 0 0 0 3.6.57 1 1 0 0 1 1 1V20a1 1 0 0 1-1 1A17 17 0 0 1 3 4a1 1 0 0 1 1-1h3.5a1 1 0 0 1 1 1c0 1.25.2 2.45.57 3.57a1 1 0 0 1-.25 1z"/></svg><span>0491 570 156</span></li>
      <li><svg width="12" height="12" viewBox="0 0 24 24"><path fill="#e8232b" d="M3 5h18v14H3zm2 2v.5l7 4.5 7-4.5V7z"/></svg><span>info@torvanecomputers-demo.com.au</span></li>
      <li><svg width="12" height="12" viewBox="0 0 24 24"><circle cx="12" cy="12" r="9" fill="none" stroke="#e8232b" stroke-width="2"/><path d="M3 12h18M12 3c3 3 3 15 0 18M12 3c-3 3-3 15 0 18" fill="none" stroke="#e8232b" stroke-width="1.5"/></svg><span>www.torvanecomputers-demo.com.au</span></li>
    </ul>
    <div class="social"><span></span><span></span><span></span></div>
  </div>
</footer>

<div class="footer-bar">&copy; <strong>TORVANE COMPUTERS</strong> - 2015. All Rights Reserved.</div>

</body>
</html>
```